Post storm repair flyer

looking for an eye catching 6x9 postcard to send out to single family home owners advertising a "Post Storm Repair Special" explaining that after the recent hurricanes its very important to have your roof checked and any repairs fixed right away before they become a bigger more costly problem and that even though your home wasn't directly hit by the storm the high wind gust could've cause unseen damage.
offer $200 off any repair *some rules may apply
Crest Roofing
877.512.TOPS
www.CrestRoofingco.example

```html
<!DOCTYPE html>
<html lang="en">
<head>
<meta charset="utf-8">
<title>Crest Roofing – Post Storm Repair Special Postcard</title>
<link rel="stylesheet" href="https://fonts.googleapis.com/css2?family=Montserrat:wght@400;500;700;800;900&family=Lexend:wght@400;500&display=swap">
<style>
  :root {
    --gold: #e8b43a;
    --badge-yellow: #ffd500;
    --black: #0d0d0d;
    --white: #ffffff;
    --offer-red: #e4121b;
    --line-grey: #c9c9c9;
    --page: #eeeae4;
    --sky: #7fa6d8;
    --roof: #5b5e66;
    --siding: #e9ecef;
  }
  * { box-sizing: border-box; margin: 0; padding: 0; }
  html, body { width: 1200px; height: 1086px; overflow: hidden; background: var(--page); }
  body { position: relative; font-family: "Montserrat", sans-serif; }

  .postcard {
    position: absolute; left: 258px; width: 684px; height: 462px;
    overflow: hidden; background: var(--white);
    box-shadow: 0 4px 14px rgba(0,0,0,.22);
  }
  .postcard--front { top: 54px; }
  .postcard--back { top: 560px; }

  /* ---------- front ---------- */
  .front-photo {
    position: absolute; inset: 0 0 102px 0;
    background: linear-gradient(180deg, var(--sky) 0%, #a9b4c2 22%, var(--roof) 34%, #6d7079 48%, var(--siding) 62%, #d7dbe0 100%);
  }
  .brand-panel {
    position: absolute; top: 0; right: 0; width: 278px; height: 139px;
    background: var(--white);
    clip-path: polygon(0 0, 100% 0, 100% 100%, 30% 100%);
    display: flex; flex-direction: column; align-items: flex-end; justify-content: center;
    padding-right: 34px;
  }
  .brand-panel__name {
    display: flex; align-items: center; gap: 7px;
    font-weight: 800; font-size: 18px; color: var(--black); letter-spacing: .5px;
  }
  .brand-panel__mark { width: 12px; height: 12px; background: var(--black); }
  .brand-panel__web { margin-top: 10px; font-size: 10px; font-weight: 500; color: var(--black); }

  .headline-band {
    position: absolute; left: 0; top: 200px; width: 510px; height: 160px;
    background: var(--gold);
    clip-path: polygon(0 0, 80% 0, 100% 100%, 0 100%);
  }
  .headline {
    position: absolute; left: 36px; top: 215px;
    font-weight: 900; font-size: 43px; line-height: 38px; color: var(--black);
    letter-spacing: -.5px; text-transform: uppercase;
  }
  .subline {
    position: absolute; left: 38px; top: 302px;
    font-family: "Lexend", sans-serif; color: var(--white); font-size: 15px; line-height: 21px;
  }
  .subline strong { font-weight: 400; font-size: 20px; }

  .contact-band {
    position: absolute; left: 0; bottom: 0; width: 100%; height: 102px;
    background: var(--black); border-top: 5px solid var(--gold);
  }
  .contact-band::before {
    content: ""; position: absolute; left: 0; top: -5px; width: 520px; height: 5px; background: var(--black);
  }
  .phone {
    position: absolute; display: flex; align-items: center; gap: 8px;
    font-weight: 600; color: var(--white); letter-spacing: .5px;
  }
  .phone svg { fill: none; stroke: var(--white); stroke-width: 2; }
  .phone--front { left: 132px; top: 385px; font-size: 24px; }

  .offer-badge { position: absolute; width: 138px; height: 158px; }
  .offer-badge svg.hex { position: absolute; inset: 0; }
  .offer-badge__text {
    position: absolute; left: 0; right: 0; top: 58px; text-align: center; color: var(--black);
    font-weight: 800; line-height: 1;
  }
  .offer-badge__get { font-size: 15px; }
  .offer-badge__amount { font-size: 25px; color: var(--offer-red); font-weight: 900; margin-top: 2px; }
  .offer-badge__what { font-size: 15px; margin-top: 2px; }
  .offer-badge__rules { font-size: 8px; font-weight: 400; font-style: italic; margin-top: 4px; color: #444; }
  .offer-badge--front { left: 514px; top: 270px; }
  .offer-badge--back { left: 274px; top: 290px; transform: scale(.82); transform-origin: top left; }

  /* ---------- back ---------- */
  .back-frame { position: absolute; inset: 0; background: var(--black); }
  .back-top-stripe {
    position: absolute; left: 0; top: 0; width: 215px; height: 30px; background: var(--gold);
    clip-path: polygon(0 0, 92% 0, 100% 100%, 0 100%);
  }
  .back-panel { position: absolute; left: 34px; top: 30px; width: 616px; height: 354px; background: var(--white); }
  .back-side-stripe { position: absolute; left: 0; top: 128px; width: 34px; height: 94px; background: var(--gold); }
  .back-title-shadow {
    position: absolute; left: 0; top: 50px; width: 360px; height: 78px; background: #e4e4e4;
    clip-path: polygon(0 0, 88% 0, 100% 100%, 0 100%);
  }
  .back-title-band {
    position: absolute; left: 0; top: 50px; width: 340px; height: 78px; background: var(--black);
    clip-path: polygon(0 0, 88% 0, 100% 100%, 0 100%);
  }
  .back-title {
    position: absolute; left: 50px; top: 68px;
    font-family: "Lexend", sans-serif; font-weight: 500; color: var(--gold);
    font-size: 24px; line-height: 21px;
  }
  .back-body {
    position: absolute; left: 42px; top: 142px; width: 260px;
    font-size: 13.5px; line-height: 16.5px; color: var(--black);
  }
  .back-photo {
    position: absolute; left: 0; top: 222px; width: 430px; height: 240px;
    background: linear-gradient(180deg, var(--sky) 0%, #b8c3cf 30%, var(--roof) 45%, #e6e8eb 62%, #8c7b6a 100%);
    clip-path: polygon(0 0, 84% 0, 100% 85%, 100% 100%, 0 100%);
  }
  .back-contact-band {
    position: absolute; left: 310px; top: 384px; width: 374px; height: 78px; background: var(--gold);
    clip-path: polygon(8% 0, 100% 0, 100% 100%, 0 100%);
  }
  .phone--back { left: 390px; top: 405px; font-size: 24px; }
  .phone--back svg { fill: var(--black); stroke: none; }

  .stamp-box { position: absolute; left: 567px; top: 62px; width: 64px; height: 67px; border: 1px solid #333; }
  .address-line { position: absolute; left: 426px; width: 204px; height: 1px; background: var(--line-grey); }
</style>
</head>
<body>

  <!-- Front side -->
  <section class="postcard postcard--front">
    <div class="front-photo" role="img" aria-label="Photo of roofers working on a white two-storey house with shingle bundles on the roof"></div>

    <div class="brand-panel">
      <div class="brand-panel__name"><span class="brand-panel__mark"></span>Crest Roofing</div>
      <div class="brand-panel__web">CRESTROOFINGCO.EXAMPLE</div>
    </div>

    <div class="headline-band"></div>
    <h1 class="headline">Post Storm<br>Repair Special</h1>
    <p class="subline">Protect Your Home. <strong>Post-Hurricane</strong><br><strong>Roof Inspections</strong> is Essential.</p>

    <div class="contact-band"></div>
    <div class="phone phone--front">
      <svg width="30" height="32" viewBox="0 0 30 32"><polygon points="15,2 27,9 27,23 15,30 3,23 3,9"/><path d="M11 10c-2 2-1 6 2 9s6 4 8 2l-2-3-2 1c-1-1-3-3-4-5l1-2z" fill="#fff" stroke="none"/></svg>
      877.512.TOPS
    </div>

    <div class="offer-badge offer-badge--front">
      <svg class="hex" viewBox="0 0 138 158" width="138" height="158">
        <polygon points="69,3 134,40 134,118 69,155 4,118 4,40" fill="var(--badge-yellow)" stroke="#fff" stroke-width="2"/>
        <polygon points="69,8 129,42 129,116 69,150 9,116 9,42" fill="none" stroke="#111" stroke-width="1"/>
        <polygon points="69,30 110,56 98,56 69,38 40,56 28,56" fill="var(--black)"/>
        <rect x="44" y="30" width="8" height="14" fill="var(--black)"/>
      </svg>
      <div class="offer-badge__text">
        <div class="offer-badge__get">Get</div>
        <div class="offer-badge__amount">$200 off</div>
        <div class="offer-badge__what">any repair</div>
        <div class="offer-badge__rules">*some rules<br>may apply</div>
      </div>
    </div>
  </section>

  <!-- Back side -->
  <section class="postcard postcard--back">
    <div class="back-frame"></div>
    <div class="back-top-stripe"></div>
    <div class="back-panel"></div>
    <div class="back-side-stripe"></div>
    <div class="back-title-shadow"></div>
    <div class="back-title-band"></div>
    <h2 class="back-title">Ensure Your Roof’s<br>Safe Today</h2>
    <p class="back-body">Even if your home wasn’t directly hit by the storm, high wind gusts can cause unseen damage.</p>

    <div class="stamp-box"></div>
    <div class="address-line" style="top:171px"></div>
    <div class="address-line" style="top:207px"></div>
    <div class="address-line" style="top:243px"></div>
    <div class="address-line" style="top:278px"></div>
    <div class="address-line" style="top:314px"></div>

    <div class="back-photo" role="img" aria-label="Photo of a roofing crew on ladders at a white house with a two-car garage"></div>
    <div class="back-contact-band"></div>
    <div class="phone phone--back">
      <svg width="26" height="26" viewBox="0 0 26 26"><path d="M5 2l5 0 2 6-3 2c1 3 4 6 7 7l2-3 6 2v5c-12 1-21-8-19-19z"/></svg>
      877.512.TOPS
    </div>

    <div class="offer-badge offer-badge--back">
      <svg class="hex" viewBox="0 0 138 158" width="138" height="158">
        <polygon points="69,3 134,40 134,118 69,155 4,118 4,40" fill="var(--badge-yellow)" stroke="#fff" stroke-width="2"/>
        <polygon points="69,8 129,42 129,116 69,150 9,116 9,42" fill="none" stroke="#111" stroke-width="1"/>
        <polygon points="69,30 110,56 98,56 69,38 40,56 28,56" fill="var(--black)"/>
        <rect x="44" y="30" width="8" height="14" fill="var(--black)"/>
      </svg>
      <div class="offer-badge__text">
        <div class="offer-badge__get">Get</div>
        <div class="offer-badge__amount">$200 off</div>
        <div class="offer-badge__what">any repair</div>
        <div class="offer-badge__rules">*some rules<br>may apply</div>
      </div>
    </div>
  </section>

</body>
</html>
```